innovative investment real estate sales firm

We are a uniquely collabrative firm that seeks to bring a conultative approach to uncovering hidden opportunities for our clients, our website needs to convey our client focused approach. Our firm specializes in the sale of apartment properties in Southern California. We have a team of researchers, transaction coordinators and marketing personal to support our geographically specialized advisers. We need a website that introduces clients to our unique way of better helping them achieve their investment goals.

Target Market(s)

High net worth individuals and families

Industry/Entity Type

Real Estate Agent

Font styles to use
Other font styles liked:
• please use font provided

Requirements
Must have
• Stories of our recent projects
• Features on our people
• email capture for viewing inventory
• content that showcases our unique consultative approach that uncovers unrealized opportunities

```html
<!DOCTYPE html>
<html lang="en">
<head>
<meta charset="utf-8">
<title>Meridian Advisers – Multifamily Properties</title>
<link href="https://fonts.googleapis.com/css2?family=Montserrat:wght@400;600;700&family=Open+Sans:ital,wght@0,400;0,600;0,700;1,700&display=swap" rel="stylesheet">
<style>
:root{
  --teal:#12a3b5;
  --teal-dark:#0e8b9b;
  --green:#9acd1c;
  --ink:#2b2f33;
  --text:#4a4f55;
  --muted:#9aa0a6;
  --grey-bg:#efefef;
  --white:#ffffff;
  --line:#cfd4d8;
}
*{box-sizing:border-box;margin:0;padding:0}
html,body{width:1200px;height:3333px;overflow:hidden}
body{background:var(--white);font-family:"Open Sans",Arial,sans-serif;color:var(--text);position:relative}
.abs{position:absolute}

/* top bar */
.top-bar{left:0;top:0;width:1200px;height:48px;background:var(--teal);color:var(--white);font-size:14px;font-weight:600;display:flex;justify-content:flex-end;align-items:center;gap:34px;padding-right:44px}
.top-bar span{display:flex;align-items:center;gap:8px}

/* header */
.site-header{left:0;top:48px;width:1200px;height:112px;background:var(--white)}
.brand{left:46px;top:34px;display:flex;align-items:center;gap:12px}
.brand-square{width:36px;height:36px;background:var(--teal);flex:none}
.brand-name{font-family:"Montserrat",sans-serif;font-weight:700;font-size:24px;letter-spacing:2px;color:var(--teal);text-transform:uppercase;white-space:nowrap}
.main-nav{right:44px;top:52px;display:flex;gap:28px;align-items:center;font-family:"Montserrat",sans-serif;font-weight:700;font-size:14px;color:var(--ink);text-transform:uppercase}

/* hero */
.hero{left:0;top:160px;width:1200px;height:556px;background:linear-gradient(180deg,#8fa4b6 0%,#b9c4cc 35%,#7d858a 70%,#3f4a3d 100%)}
.hero-shade{position:absolute;inset:0;background:rgba(20,30,40,.25)}
.hero-title{position:absolute;top:212px;left:0;width:1200px;text-align:center;font-family:"Montserrat",sans-serif;font-weight:700;font-size:30px;color:var(--white);letter-spacing:1px}
.hero-title em{font-style:normal;color:var(--teal)}
.hero-text{position:absolute;top:270px;left:300px;width:600px;text-align:center;font-size:16px;line-height:22px;color:var(--white)}
.hero-arrow{position:absolute;top:256px;width:44px;height:44px;background:var(--teal);display:flex;align-items:center;justify-content:center}

/* section headings */
.section-heading{left:0;width:1200px;display:flex;justify-content:center;align-items:center;gap:18px;font-family:"Montserrat",sans-serif;font-weight:700;font-size:26px;color:var(--ink);text-transform:uppercase}
.section-heading .rule{width:60px;height:2px;background:var(--line)}
.section-heading .mark{width:30px;height:30px;background:var(--teal)}
.section-heading em{font-style:normal;color:var(--green)}

.btn{display:flex;align-items:center;justify-content:center;background:var(--teal);color:var(--white);font-family:"Montserrat",sans-serif;font-weight:700;font-size:15px;text-transform:uppercase;border-radius:3px}

/* about */
.about-text{left:96px;top:852px;width:1008px;text-align:center;font-size:13.5px;line-height:22px;color:var(--text)}

/* people */
.people{left:0;top:1090px;width:1200px;height:506px;background:var(--grey-bg)}
.person{width:220px;text-align:center}
.person-photo{width:200px;height:200px;margin:0 auto;border-radius:50%;border:8px solid var(--white);box-shadow:0 0 0 2px #e2e2e2;background:linear-gradient(180deg,#d9d4cf 0%,#b89a82 55%,#3a4250 100%)}
.person-name{margin-top:22px;font-family:"Montserrat",sans-serif;font-weight:700;font-size:16px;color:var(--teal)}
.person-role{font-family:"Montserrat",sans-serif;font-weight:600;font-size:15px;color:var(--ink);margin-top:2px}
.person-social{margin-top:20px;display:flex;justify-content:center;gap:10px}
.person-social i{width:14px;height:14px;border-radius:50%;background:#b9bec3;display:block}
.chev{font-family:"Montserrat",sans-serif;font-size:44px;color:#c6c9cc}

/* services */
.service-icon{width:124px;height:124px;border-radius:50%;border:4px solid var(--teal)}
.service-title{font-family:"Montserrat",sans-serif;font-weight:600;font-size:17px;color:var(--teal)}
.service-text{width:400px;font-size:13.5px;line-height:20px;color:var(--text)}

/* approach */
.approach{left:0;top:1978px;width:1200px;height:495px;background:var(--grey-bg)}
.step{position:absolute;width:190px;text-align:center;font-size:14px;line-height:18px;color:var(--ink)}
.step h3{font-family:"Montserrat",sans-serif;font-weight:700;font-size:16px;color:var(--teal);text-transform:uppercase;margin-bottom:2px}

/* testimonials */
.quote-box{left:251px;top:2615px;width:698px;height:140px;border:2px solid #dcdcdc;border-radius:8px;background:#fafafa;padding:22px 30px 0 30px;font-size:14px;line-height:21px;color:var(--text)}
.quote-mark{font-family:"Montserrat",sans-serif;font-weight:700;font-size:44px;color:var(--ink);line-height:0;vertical-align:-16px}
.quote-author{left:256px;top:2772px;font-weight:700;font-style:italic;font-size:16px;color:var(--ink)}
.dots{left:572px;top:2820px;display:flex;gap:5px}
.dots i{display:block;width:11px;height:11px;border-radius:50%;border:1.5px solid var(--teal)}
.dots i.on{background:var(--teal)}

/* footer */
.site-footer{left:0;top:2911px;width:1200px;height:378px;background:var(--teal);color:var(--white)}
.footer-brand{position:absolute;top:56px;left:0;width:1200px;display:flex;justify-content:center;align-items:center;gap:14px}
.footer-brand .brand-square{background:var(--white);width:40px;height:40px}
.footer-brand .brand-name{color:var(--white);font-size:30px}
.footer-col{position:absolute;top:142px;font-size:12px;line-height:17px;font-weight:600}
.footer-col h4{font-family:"Montserrat",sans-serif;font-weight:700;font-size:14px;text-transform:uppercase;padding-bottom:10px;border-bottom:1px solid rgba(255,255,255,.5);margin-bottom:14px;width:150px}
.contact-row{display:flex;gap:8px;margin-bottom:12px}
.contact-row .ico{width:18px;height:18px;border:1.5px solid var(--white);border-radius:50%;flex:none;display:flex;align-items:center;justify-content:center}
.newsletter{display:flex}
.newsletter .field{width:167px;height:36px;background:var(--white);color:var(--ink);font-size:13px;font-weight:700;padding:9px 8px}
.newsletter .submit{width:91px;height:36px;background:#222;color:var(--white);font-family:"Montserrat",sans-serif;font-weight:700;font-size:13px;display:flex;align-items:center;justify-content:center}
.copyright{left:0;top:3289px;width:1200px;height:44px;display:flex;align-items:center;justify-content:center;font-size:11px;font-weight:700;color:var(--ink);letter-spacing:.3px}
</style>
</head>
<body>

<div class="abs top-bar">
  <span><svg width="14" height="14" viewBox="0 0 24 24"><path fill="#fff" d="M6.6 10.8a15 15 0 0 0 6.6 6.6l2.2-2.2c.3-.3.7-.4 1-.2 1.1.4 2.3.6 3.6.6.6 0 1 .4 1 1V20c0 .6-.4 1-1 1A17 17 0 0 1 3 4c0-.6.4-1 1-1h3.5c.6 0 1 .4 1 1 0 1.3.2 2.5.6 3.6.1.3 0 .7-.2 1z"/></svg>+44 (0) 7000 123456</span>
  <span><svg width="15" height="12" viewBox="0 0 24 18"><rect x="1" y="1" width="22" height="16" fill="none" stroke="#fff" stroke-width="2"/><path d="M1 1l11 9 11-9" fill="none" stroke="#fff" stroke-width="2"/></svg>info@meridianadvisers.com</span>
</div>

<header class="abs site-header">
  <div class="abs brand"><div class="brand-square"></div><div class="brand-name">Meridian Advisers</div></div>
  <nav class="abs main-nav">
    <svg width="18" height="16" viewBox="0 0 24 20"><path fill="#12a3b5" d="M12 0l12 10h-3v10h-6v-6H9v6H3V10H0z"/></svg>
    <span>About</span><span>Our People</span><span>Services</span><span>Approach</span><span>Testimonials</span><span>Contact</span>
  </nav>
</header>

<section class="abs hero" role="img" aria-label="Photograph of a modern white multi-storey apartment building with large glass windows">
  <div class="hero-shade"></div>
  <h1 class="hero-title">WELCOME TO <em>MERIDIAN ADVISERS</em></h1>
  <p class="hero-text">Our firm specializes in the sale of apartment properties in Southern California. We have a team of researchers, transaction coordinators and marketing personal to support our geographically specialized advisers.</p>
  <div class="hero-arrow" style="left:0"><svg width="14" height="18" viewBox="0 0 14 18"><path d="M11 2L4 9l7 7" fill="none" stroke="#fff" stroke-width="3"/></svg></div>
  <div class="hero-arrow" style="right:0"><svg width="14" height="18" viewBox="0 0 14 18"><path d="M3 2l7 7-7 7" fill="none" stroke="#fff" stroke-width="3"/></svg></div>
</section>

<!-- about -->
<h2 class="abs section-heading" style="top:774px"><span class="rule"></span><span class="mark"></span><span>About <em>Us</em></span><span class="rule"></span></h2>
<p class="abs about-text">Lorem ipsum dolor sit amet, consectetuer adipiscing elit, sed diam nonummy nibh euismod tincidunt ut laoreet dolore magna aliquam erat volutpat. Ut wisi enim ad minim veniam, quis nostrud exerci tation ullamcorper suscipit lobortis nisl ut aliquip ex ea commodo consequat. Duis autem vel eum iriure dolor in hendrerit in vulputate velit esse molestie consequat, vel illum dolore eu feugiat nulla facilisis at vero eros et accumsan et iusto odio dignissim qui blandit praesent luptatum zzril delenit augue duis dolore te feugait nulla facilisi. Nam liber tempor cum soluta nobis eleifend option congue nihil imperdiet doming id quod mazim placerat facer possim assum.</p>
<div class="abs btn" style="left:505px;top:998px;width:190px;height:36px">Learn More</div>

<!-- people -->
<section class="abs people">
  <h2 class="abs section-heading" style="top:58px"><span class="rule"></span><span class="mark"></span><span>Our <em>People</em></span><span class="rule"></span></h2>
  <div class="abs chev" style="left:62px;top:208px">&#8249;</div>
  <div class="abs chev" style="left:1108px;top:208px">&#8250;</div>
  <div class="abs person" style="left:143px;top:143px"><div class="person-photo" role="img" aria-label="Portrait photo of Tobin Ashcroft"></div><div class="person-name">Tobin Ashcroft</div><div class="person-role">Founder &amp; CEO</div><div class="person-social"><i></i><i></i><i></i><i></i></div></div>
  <div class="abs person" style="left:377px;top:143px"><div class="person-photo" role="img" aria-label="Portrait photo of Marcus Dale"></div><div class="person-name">Marcus Dale</div><div class="person-role">Co-Founder &amp; CFO</div><div class="person-social"><i></i><i></i><i></i><i></i></div></div>
  <div class="abs person" style="left:606px;top:143px"><div class="person-photo" role="img" aria-label="Portrait photo of Elise Marlow"></div><div class="person-name">Elise Marlow</div><div class="person-role">COO</div><div class="person-social"><i></i><i></i><i></i><i></i></div></div>
  <div class="abs person" style="left:834px;top:143px"><div class="person-photo" role="img" aria-label="Portrait photo of Nora Whitfield"></div><div class="person-name">Nora Whitfield</div><div class="person-role">CTO</div><div class="person-social"><i></i><i></i><i></i><i></i></div></div>
</section>

<!-- services -->
<h2 class="abs section-heading" style="top:1654px"><span class="rule"></span><span class="mark"></span><span><em>Services</em></span><span class="rule"></span></h2>
<div class="abs service-icon" style="left:54px;top:1734px">
  <svg width="116" height="116" viewBox="0 0 116 116"><circle cx="46" cy="50" r="12" fill="#12a3b5"/><path d="M24 88c0-14 10-22 22-22s22 8 22 22z" fill="#12a3b5"/><rect x="60" y="30" width="30" height="24" fill="none" stroke="#12a3b5" stroke-width="3"/><path d="M68 46v-7l7-5 7 5v7z" fill="#12a3b5"/></svg>
</div>
<div class="abs service-title" style="left:187px;top:1736px">Property Investment Consulting</div>
<p class="abs service-text" style="left:187px;top:1760px">Lorem ipsum dolor sit amet, consectetuer adipiscing elit, sed diam nonummy nibh euismod tincidunt ut laoreet dolore magna aliquam erat volutpat. Ut wisi enim ad minim veniam, quis nostrud exerci tation ullamcorper suscipit lobortis nisl ut aliquip ex ea commodo.</p>
<div class="abs btn" style="left:184px;top:1890px;width:190px;height:36px">Learn More</div>

<div class="abs service-icon" style="left:628px;top:1734px">
  <svg width="116" height="116" viewBox="0 0 116 116"><rect x="34" y="30" width="48" height="58" fill="#12a3b5"/><g fill="#fff"><rect x="40" y="38" width="8" height="8"/><rect x="54" y="38" width="8" height="8"/><rect x="68" y="38" width="8" height="8"/><rect x="40" y="52" width="8" height="8"/><rect x="54" y="52" width="8" height="8"/><rect x="68" y="52" width="8" height="8"/><rect x="52" y="70" width="12" height="18"/></g></svg>
</div>
<div class="abs service-title" style="left:760px;top:1736px">Sales of Apartment Properties</div>
<p class="abs service-text" style="left:760px;top:1760px">Lorem ipsum dolor sit amet, consectetuer adipiscing elit, sed diam nonummy nibh euismod tincidunt ut laoreet dolore magna aliquam erat volutpat. Ut wisi enim ad minim veniam, quis nostrud exerci tation ullamcorper suscipit lobortis nisl ut aliquip ex ea commodo.</p>
<div class="abs btn" style="left:758px;top:1890px;width:190px;height:36px">Learn More</div>

<!-- approach -->
<section class="abs approach">
  <h2 class="abs section-heading" style="top:62px"><span class="rule"></span><span class="mark"></span><span>Our <em>Approach</em></span><span class="rule"></span></h2>
  <svg class="abs" style="left:0;top:0" width="1200" height="495" viewBox="0 0 1200 495">
    <path d="M193 287 A158 158 0 0 0 509 287 L477 287 A126 126 0 0 1 225 287 Z" fill="#12a3b5"/>
    <path d="M686 287 A158 158 0 0 0 1002 287 L970 287 A126 126 0 0 1 718 287 Z" fill="#12a3b5"/>
    <path d="M451 300 L451 287 A149 149 0 0 1 749 287 L749 300 L717 300 L717 287 A117 117 0 0 0 483 287 L483 300 Z" fill="#9acd1c"/>
    <circle cx="346" cy="262" r="107" fill="#fff"/>
    <circle cx="600" cy="283" r="107" fill="#fff"/>
    <circle cx="854" cy="262" r="107" fill="#fff"/>
  </svg>
  <div class="step" style="left:251px;top:224px"><h3>Consulting</h3>Clients approach us with<br>their investment goals</div>
  <div class="step" style="left:505px;top:212px"><h3>Our Expertise</h3>We have a team of researchers, transaction coordinators and marketing personal to support our geographically specialized advisers.</div>
  <div class="step" style="left:759px;top:210px"><h3>Reach Goals</h3>We present the ideal solutions and unique way of better helping clients achieving their investment goals.</div>
</section>

<!-- testimonials -->
<h2 class="abs section-heading" style="top:2532px"><span class="rule"></span><span class="mark"></span><span>What Clients <em>Say</em></span><span class="rule"></span></h2>
<div class="abs quote-box"><span class="quote-mark">&ldquo;</span> Lorem ipsum dolor sit amet, consectetuer adipiscing elit, sed diam nonummy nibh euismod tincidunt ut laoreet dolore magna aliquam erat volutpat. Ut wisi enim ad minim veniam, quis nostrud exercitation ullamcorper suscipit lobortis nisl ut aliquip ex ea commodo conse quat. Duis autem vel eum iriure dolor in hendrerit in vulputate velit esse. <span class="quote-mark">&rdquo;</span></div>
<div class="abs quote-author">Peter Langford</div>
<div class="abs dots"><i class="on"></i><i></i><i></i><i></i></div>

<!-- footer -->
<footer class="abs site-footer">
  <div class="footer-brand"><div class="brand-square"></div><div class="brand-name">Meridian Advisers</div></div>
  <div class="footer-col" style="left:122px"><h4>Quick Links</h4>Home<br>About<br>Our People<br>Services<br>Approach<br>Testimonials<br>Contact</div>
  <div class="footer-col" style="left:296px"><h4>Services</h4>Property Investment Consulting<br>Sale of Apartment Properties</div>
  <div class="footer-col" style="left:558px"><h4>Contact</h4>
    <div class="contact-row"><span class="ico"><svg width="8" height="10" viewBox="0 0 8 10"><path d="M4 0a4 4 0 0 1 4 4c0 3-4 6-4 6S0 7 0 4a4 4 0 0 1 4-4z" fill="#fff"/></svg></span><span>Meridian Advisers<br>456 Sample Ave<br>Suite #200<br>Los Angeles, CA 90001</span></div>
    <div class="contact-row"><span class="ico"><svg width="9" height="9" viewBox="0 0 24 24"><path fill="#fff" d="M6.6 10.8a15 15 0 0 0 6.6 6.6l2.2-2.2c.3-.3.7-.4 1-.2 1.1.4 2.3.6 3.6.6.6 0 1 .4 1 1V20c0 .6-.4 1-1 1A17 17 0 0 1 3 4c0-.6.4-1 1-1h3.5c.6 0 1 .4 1 1 0 1.3.2 2.5.6 3.6.1.3 0 .7-.2 1z"/></svg></span><span>+44 (0) 7000 123456</span></div>
    <div class="contact-row"><span class="ico"><svg width="9" height="7" viewBox="0 0 24 18"><rect x="1" y="1" width="22" height="16" fill="none" stroke="#fff" stroke-width="3"/></svg></span><span>info@meridianadvisers.com</span></div>
  </div>
  <div class="footer-col" style="left:822px"><h4 style="width:258px">Newsletter Sign Up</h4>
    <div class="newsletter"><div class="field">Enter Email Address</div><div class="submit">SIGN UP</div></div>
  </div>
</footer>
<div class="abs copyright">© COPYRIGHT 2017 MERIDIAN ADVISERS. ALL RIGHTS RESERVED</div>

</body>
</html>
```